A4 Block Hour Agreement Brochure

We need a new Block Hour Agreement Brochure created as our current one lacks design and is ugly. The current block hour agreement brochure has been attached "pixelharbor.pdf".

We are looking at a modern brochure and have attached "Vellamore Private Cloud Plans.pdf" as an example.

It doesnt have to be the exact same design, but it must be the "Vellamore blue" theme.

Target Market(s)

Information Technology

Colors
0054AA
0677BA
7BADD7
CADEEF
E8F1F8

```html
<!DOCTYPE html>
<html lang="en">
<head>
<meta charset="utf-8">
<title>Block Hour Agreement – Vellamore Technologies</title>
<link href="https://fonts.googleapis.com/css2?family=Montserrat:ital,wght@0,400;0,500;0,600;0,700;0,800;0,900;1,500&display=swap" rel="stylesheet">
<style>
  :root {
    --navy: #1e2468;
    --blue-deep: #0054AA;
    --blue-mid: #0677BA;
    --blue-light: #7BADD7;
    --blue-pale: #CADEEF;
    --blue-mist: #E8F1F8;
    --grey-band: #c6c6c6;
    --grey-dark: #9a9a9a;
    --white: #ffffff;
    --ink: #111111;
  }
  * { box-sizing: border-box; margin: 0; padding: 0; }
  html, body { width: 1174px; height: 1200px; overflow: hidden; background: var(--white); }
  body { font-family: "Montserrat", Arial, sans-serif; position: relative; }

  .brochure {
    position: absolute; left: 261px; top: 139px;
    width: 652px; height: 922px;
    border: 1px solid #cfcfcf; background: var(--white); overflow: hidden;
  }
  .brochure__shapes { position: absolute; inset: 0; }

  .brand { position: absolute; left: 32px; top: 36px; display: flex; align-items: center; gap: 10px; }
  .brand__mark { width: 34px; height: 34px; border-radius: 50%; background: var(--blue-deep); }
  .brand__name { font-weight: 800; font-size: 19px; letter-spacing: 1px; color: var(--navy); text-transform: uppercase; }

  .headline {
    position: absolute; left: 50px; top: 146px;
    color: var(--white); font-weight: 900; font-size: 54px; line-height: 53px; letter-spacing: -0.5px;
  }

  .tab {
    position: absolute; display: flex; align-items: center;
    color: var(--navy); font-weight: 800; background: var(--grey-band);
  }
  .tab--overview { left: 50px; top: 287px; width: 203px; height: 35px; padding-left: 17px; font-size: 28px;
    clip-path: polygon(0 0, 100% 0, 92% 100%, 0 100%); }
  .tab--types { left: 339px; top: 618px; width: 226px; height: 25px; padding-left: 12px; font-size: 19px;
    clip-path: polygon(0 0, 100% 0, 94% 100%, 0 100%); }

  .overview { position: absolute; left: 50px; top: 342px; color: var(--white);
    font-size: 9.2px; line-height: 13.1px; font-weight: 400; }
  .overview p { margin-bottom: 13.1px; }
  .overview .line { display: block; width: var(--w, auto); white-space: nowrap;
    text-align: justify; text-align-last: justify; }
  .overview .line--last { text-align-last: left; }

  .rule { position: absolute; left: 50px; top: 582px; width: 414px; height: 1px; background: var(--blue-pale); opacity: .8; }

  .terms { position: absolute; left: 50px; top: 617px; list-style: none; color: var(--white);
    font-weight: 600; font-size: 11.8px; line-height: 14.2px; }
  .terms li { position: relative; padding-left: 24px; margin-bottom: 9.5px; }
  .terms li::before {
    content: ""; position: absolute; left: 0; top: 1px; width: 9px; height: 9px;
    border-top: 2.4px solid var(--blue-pale); border-right: 2.4px solid var(--blue-pale);
    transform: rotate(45deg) translate(-1px, 2px);
  }

  .pricing { position: absolute; left: 339px; top: 649px; width: 276px; border-collapse: separate; border-spacing: 3px 0; margin-left: -3px; }
  .pricing th { background: var(--blue-mid); color: var(--white); font-weight: 700; font-size: 12.2px; height: 22px; text-align: center; }
  .pricing td { background: var(--white); color: var(--ink); font-weight: 600; font-size: 12.2px; height: 23.2px; text-align: center; }
  .pricing tr:nth-child(even) td { background: var(--grey-band); }

  .legal { position: absolute; left: 339px; top: 941px; width: 276px; text-align: center;
    color: var(--blue-pale); font-style: italic; font-weight: 500; font-size: 5.6px; line-height: 11px; }

  .contact { position: absolute; top: 882px; display: flex; align-items: center; gap: 8px; color: var(--navy); }
  .contact--phone { left: 44px; font-weight: 800; font-size: 19.5px; }
  .contact--email { left: 233px; font-weight: 500; font-size: 18.6px; }
  .contact__icon { width: 18px; height: 18px; }
</style>
</head>
<body>
<main class="brochure">
  <svg class="brochure__shapes" width="652" height="922" viewBox="0 0 652 922">
    <defs>
      <linearGradient id="panelGrad" x1="0" y1="0" x2="0.25" y2="1">
        <stop offset="0" stop-color="#123f9e"/>
        <stop offset="0.45" stop-color="#1d2f88"/>
        <stop offset="1" stop-color="#2a1763"/>
      </linearGradient>
      <linearGradient id="photoGrad" x1="0" y1="0" x2="1" y2="0.3">
        <stop offset="0" stop-color="#cfd3d8"/>
        <stop offset="0.45" stop-color="#f2f2f2"/>
        <stop offset="0.7" stop-color="#c99a82"/>
        <stop offset="1" stop-color="#1c1c22"/>
      </linearGradient>
    </defs>
    <polygon points="472,79 634,0 652,0 496,79" fill="var(--grey-band)"/>
    <polygon points="137,79 652,79 652,853 0,853 0,116 156,116" fill="url(#panelGrad)"/>
    <polygon points="521,107 652,330 652,582 243,582" fill="url(#photoGrad)" role="img"
      aria-label="Photo of a hand holding an hourglass in front of a businessman's suit"/>
    <polygon points="0,853 305,853 293,864 0,864" fill="var(--grey-dark)"/>
  </svg>

  <div class="brand">
    <span class="brand__mark"></span>
    <span class="brand__name">Vellamore Technologies</span>
  </div>

  <h1 class="headline">BLOCK HOUR<br>AGREEMENT</h1>

  <h2 class="tab tab--overview">OVERVIEW</h2>

  <section class="overview">
    <p>
      <span class="line" style="--w:290px">Vellamore Technologies offers the Block Time Service Agree-</span>
      <span class="line" style="--w:284px">ment at a discounted hourly rate for clients who need consis-</span>
      <span class="line" style="--w:278px">tent support throughout a period of time. A block time agree-</span>
      <span class="line" style="--w:272px">ment lets you pre-pay for services and call upon them as</span>
      <span class="line line--last">needed, this allows for easy accounting and easy support.</span>
    </p>
    <p>
      <span class="line line--last">Our Block Time Service Agreement can be used for all</span>
      <span class="line line--last">non-project related work, please ask your Vellamore</span>
      <span class="line line--last">representative for more details.</span>
    </p>
    <p>
      <span class="line line--last">Block hours are not covered under a Service Level</span>
      <span class="line" style="--w:222px">Agreement (SLA) and are best effort, while we</span>
      <span class="line" style="--w:216px">endeavor to always provide prompt service to</span>
      <span class="line" style="--w:210px">our customers in some situations such as a</span>
      <span class="line" style="--w:203px">service disruption, it may not always be</span>
      <span class="line line--last">possible to attend straight away.</span>
    </p>
  </section>

  <div class="rule"></div>

  <ul class="terms">
    <li>Block hours do not rollover</li>
    <li>There is no set usage per week.</li>
    <li>Project services cannot be used<br>with block time.</li>
    <li>Time is billed in 0.5 hour increments with<br>a minimum of 1 hour for onsite callouts.</li>
    <li>Hours must be used within 12 months<br>of purchase.</li>
    <li>Hours must be used during standard<br>business hours 8:30am-5pm AWST.<br>After hours is charged at double time.</li>
  </ul>

  <h2 class="tab tab--types">AGREEMENT TYPES</h2>

  <table class="pricing">
    <thead>
      <tr><th>HOURS</th><th>HOURLY RATE</th><th>COST (EX GST)</th></tr>
    </thead>
    <tbody>
      <tr><td>1</td><td>$270.00</td><td>$265.00</td></tr>
      <tr><td>10</td><td>$240.00</td><td>$2,400.00</td></tr>
      <tr><td>20</td><td>$225.00</td><td>$4,500.00</td></tr>
      <tr><td>35</td><td>$220.00</td><td>$7,700.00</td></tr>
      <tr><td>50</td><td>$210.00</td><td>$10,500.00</td></tr>
    </tbody>
  </table>

  <p class="legal">By engaging with Vellamore in goods/services you agree to our Terms and Conditions<br>available at https://www.vellamoretechnologies.com.au/t&amp;c</p>

  <div class="contact contact--phone">
    <svg class="contact__icon" viewBox="0 0 18 18" aria-hidden="true">
      <circle cx="9" cy="9" r="9" fill="var(--navy)"/>
      <path d="M6 4.5c.6 0 1.6 2 1.4 2.5l-.8.8c.5 1.3 1.6 2.4 2.9 2.9l.8-.8c.5-.2 2.5.8 2.5 1.4 0 .9-1 1.9-1.9 1.7C8.4 12.4 5.6 9.6 4.9 6.4 4.7 5.5 5.1 4.5 6 4.5z" fill="var(--white)"/>
    </svg>
    <span>08 9555 0142</span>
  </div>
  <div class="contact contact--email">
    <svg class="contact__icon" viewBox="0 0 18 18" aria-hidden="true">
      <circle cx="9" cy="9" r="9" fill="var(--navy)"/>
      <rect x="4.5" y="6" width="9" height="6.2" fill="none" stroke="var(--white)" stroke-width="1"/>
      <path d="M4.5 6l4.5 3.6L13.5 6" fill="none" stroke="var(--white)" stroke-width="1"/>
    </svg>
    <span>sales@vellamoretechnologies.com.au</span>
  </div>
</main>
</body>
</html>
```